Team Member Spotlight 'Stats Card' Design for ProfilNet

We are creating a 'Stats Card'-style team member spotlight post for our company's ProfilNet page. The design should be professional yet fun, reflecting our company's approachable and innovative brand. Here’s what we need:

Header featuring:
Name: Reed Calloway
Role: Area Sales Manager - Austin, TX
Photo: Will provide
Quick stats section with bold, modern fonts:
Years in Pain Management: 8 years
Time at OKRA VENT QS: 1 year (by February)
Favorite Quote: “Nothing in the world can take the place of persistence.” – Ambrose Thistlewood
Hobby/Passion: Making music (on Tunevault as Reed Calloway!)
Football Team: Pelham Tech (Herons)

Use vibrant, approachable company branding colors.
Incorporate small themed icons (e.g., music notes, football elements).
Clean, modern layout with clear sections and engaging visuals.
Subtle background details that hint at music and Texas without overpowering the content.

Optimized for ProfilNet dimensions (square or portrait format).
Delivered in editable file formats (Canva) for future use.

Professional but approachable.
Engaging design that will catch attention while staying on-brand.
We will provide the company branding guide, Reed’s photo, and detailed stats. The design should feel cohesive with our brand and stand out on ProfilNet.

Industry/Entity Type

Medical Device / Physicians

Colors

Designer to choose colors to be used in the design.

Requirements
Must have
• Include OKRA VENT QS logo & Company Colors: #a9218f & #011842

```html
<!DOCTYPE html>
<html lang="en">
<head>
<meta charset="utf-8">
<title>Team Spotlight – Reed Calloway</title>
<link rel="stylesheet" href="https://fonts.googleapis.com/css2?family=Barlow+Semi+Condensed:wght@500;600;700&display=swap">
<style>
  :root {
    --navy: #1d2046;
    --navy-deep: #171a3b;
    --magenta: #a9218f;
    --violet: #6b2f8f;
    --line-blue: #3a78c9;
    --icon-pink: #c23a9e;
    --icon-violet: #5a2d8c;
    --white: #ffffff;
  }
  * { margin: 0; padding: 0; box-sizing: border-box; }
  html, body { width: 1200px; height: 1199px; overflow: hidden; background: var(--navy); }
  body { font-family: "Barlow Semi Condensed", "Arial Narrow", sans-serif; color: var(--white); }

  .card { position: relative; width: 1200px; height: 1199px; overflow: hidden; }
  .backdrop { position: absolute; inset: 0; }

  .brand {
    position: absolute; left: 5px; top: 27px; width: 370px; height: 139px;
    border-radius: 0 70px 70px 0;
    background: linear-gradient(90deg, var(--magenta) 0%, var(--violet) 100%);
  }
  .brand-name { position: absolute; left: 42px; top: 20px; font-size: 58px; font-weight: 600; letter-spacing: 1px; line-height: 1; white-space: nowrap; }
  .brand-tag { position: absolute; left: 258px; top: 90px; font-size: 30px; font-weight: 600; line-height: 1; }

  .name-tab {
    position: absolute; left: 390px; top: 181px; width: 380px; height: 89px;
    background: var(--navy-deep); border: 2px solid var(--line-blue); border-right: none;
    border-radius: 50px 0 0 0;
    display: flex; align-items: center; justify-content: center;
    font-size: 56px; font-weight: 600; padding-left: 14px; white-space: nowrap;
  }
  .role-tab {
    position: absolute; left: 390px; top: 287px; width: 410px; height: 98px;
    border-radius: 0 0 0 50px;
    background: linear-gradient(90deg, var(--magenta) 0%, var(--violet) 100%);
    padding: 12px 0 0 62px; font-size: 30px; font-weight: 600; line-height: 40px;
  }
  .role-tab span { display: block; }
  .role-tab .city { padding-left: 8px; }

  .portrait {
    position: absolute; left: 786px; top: 113px; width: 352px; height: 352px; border-radius: 50%;
    background: radial-gradient(circle at 55% 45%, #6a5346 0%, #3b2b27 55%, #1f2542 100%);
  }

  .stat {
    position: absolute; font-size: 32px; font-weight: 600; line-height: 45px; white-space: nowrap;
    background: linear-gradient(90deg, rgba(169,33,143,0.85), rgba(120,50,160,0.75));
  }
  .stat-team { left: 0; top: 500px; width: 558px; height: 131px; border-radius: 0 26px 26px 0; padding: 20px 0 0 72px; }
  .stat-tenure { left: 0; top: 657px; width: 416px; height: 119px; border-radius: 0 26px 26px 0; padding: 14px 0 0 82px; }
  .stat-years { left: 714px; top: 654px; width: 486px; height: 126px; border-radius: 30px 0 0 30px; padding: 20px 0 0 16px; }
  .stat-hobby { left: 579px; top: 797px; width: 621px; height: 131px; border-radius: 40px 0 0 40px; padding: 20px 0 0 14px; }
  .team-icon { position: absolute; left: 392px; top: 26px; width: 96px; height: 80px; }
  .music-icon { position: absolute; left: 478px; top: 20px; width: 86px; height: 86px; }

  .quote-box {
    position: absolute; left: 86px; top: 996px; width: 444px; height: 164px;
    border-radius: 60px; background: var(--navy-deep); border: 2px solid var(--line-blue);
  }
  .quote-label { position: absolute; left: 136px; top: 1000px; font-size: 36px; font-weight: 600; }
  .quote-text {
    position: absolute; left: 106px; top: 1050px; width: 985px; height: 52px; border-radius: 26px;
    background: linear-gradient(90deg, var(--magenta) 0%, var(--violet) 100%);
    padding-left: 40px; font-size: 36px; font-weight: 600; line-height: 50px; white-space: nowrap;
  }
  .quote-author { position: absolute; left: 136px; top: 1100px; font-size: 36px; font-weight: 600; }
</style>
</head>
<body>
<main class="card">
  <svg class="backdrop" width="1200" height="1199" viewBox="0 0 1200 1199" aria-hidden="true">
    <defs>
      <linearGradient id="bg-fade" x1="0" y1="0" x2="1" y2="1">
        <stop offset="0" stop-color="#1d2046"/>
        <stop offset="0.55" stop-color="#2b2555"/>
        <stop offset="1" stop-color="#6d2f8e"/>
      </linearGradient>
      <linearGradient id="arc-fill" x1="0" y1="0" x2="1" y2="1">
        <stop offset="0" stop-color="#a9218f"/>
        <stop offset="1" stop-color="#5b2d86"/>
      </linearGradient>
    </defs>
    <rect width="1200" height="1199" fill="url(#bg-fade)"/>
    <path d="M785 0 H1200 V618 A560 560 0 0 1 785 0 Z" fill="url(#arc-fill)" opacity="0.9"/>
    <path d="M785 0 A560 560 0 0 0 1200 618" fill="none" stroke="#3a78c9" stroke-width="2"/>
    <path d="M307 0 V1199" stroke="#3a78c9" stroke-width="2" opacity="0.7"/>
    <path d="M498 0 V380 C498 700 700 1000 1000 1199" fill="none" stroke="#3a78c9" stroke-width="2" opacity="0.7"/>
    <circle cx="963" cy="288" r="208" fill="none" stroke="#d78fd0" stroke-width="14" opacity="0.6"/>
    <circle cx="963" cy="288" r="192" fill="#23244a" stroke="#3a78c9" stroke-width="3"/>
    <g fill="#ffffff" opacity="0.12">
      <circle cx="738" cy="52" r="25"/>
      <circle cx="630" cy="158" r="62"/>
      <circle cx="812" cy="566" r="57"/>
      <circle cx="735" cy="905" r="30"/>
      <circle cx="1000" cy="920" r="22"/>
      <circle cx="1110" cy="950" r="34"/>
      <circle cx="955" cy="1005" r="48"/>
      <circle cx="1045" cy="1060" r="90"/>
      <circle cx="955" cy="1118" r="36"/>
      <circle cx="655" cy="1122" r="24"/>
    </g>
    <circle cx="537" cy="698" r="20" fill="none" stroke="#3a78c9" stroke-width="2" opacity="0.5"/>
  </svg>

  <header>
    <div class="brand">
      <span class="brand-name">OKRA VENT</span>
      <span class="brand-tag">QS</span>
    </div>
    <h1 class="name-tab">Reed Calloway</h1>
    <p class="role-tab"><span>Area Sales Manager</span><span class="city">Austin, TX</span></p>
    <div class="portrait" role="img" aria-label="Portrait photo of Reed Calloway in a navy suit"></div>
  </header>

  <section class="stats">
    <div class="stat stat-team">Football Team:<br>Pelham Tech (Herons)
      <svg class="team-icon" viewBox="0 0 96 80" aria-hidden="true">
        <g transform="rotate(-30 48 40)">
          <ellipse cx="48" cy="40" rx="40" ry="24" fill="var(--icon-pink)"/>
          <path d="M30 40 H66" stroke="#ffffff" stroke-width="4" stroke-linecap="round"/>
          <path d="M38 33 V47 M46 33 V47 M54 33 V47" stroke="#ffffff" stroke-width="3.5" stroke-linecap="round"/>
        </g>
      </svg>
    </div>
    <div class="stat stat-tenure">Time at OKRA VENT QS:<br>1 year (by February)</div>
    <div class="stat stat-years">Years in Pain Management:<br>8 years</div>
    <div class="stat stat-hobby">Hobby/Passion: Making music<br>(on Tunevault as Reed Calloway!)
      <svg class="music-icon" viewBox="0 0 86 86" aria-hidden="true">
        <circle cx="43" cy="43" r="42" fill="var(--icon-violet)"/>
        <path d="M35 58 V26 L60 20 V52" fill="none" stroke="#ffffff" stroke-width="4.5" stroke-linejoin="round"/>
        <ellipse cx="29" cy="59" rx="8" ry="6" fill="#ffffff"/>
        <ellipse cx="54" cy="53" rx="8" ry="6" fill="#ffffff"/>
      </svg>
    </div>
  </section>

  <section class="quote">
    <div class="quote-box" aria-hidden="true"></div>
    <p class="quote-label">Favorite Quote:</p>
    <p class="quote-text">“Nothing in the world can take the place of persistence.”</p>
    <p class="quote-author">Ambrose Thistlewood</p>
  </section>
</main>
</body>
</html>
```